Homepage web design

I need a homepage design that will be easy to build into a default Word Press theme. Basically, header, navigation, body with sidebar, and footer.

This website is for a small commercial real estate firm in the Washington DC, Maryland and Virginia market.

THIS IS NOT A HOUSING/RESIDENTIAL WEBSITE. PLEASE DO NOT ADD ANY PROPERTY SEARCH FUNCTIONALITY.

Target Market(s)

People looking for basic information about the team and services provided.

Industry/Entity Type

Real Estate

Requirements
Must have
• Professional look. Clean design.

```html
<!DOCTYPE html>
<html lang="en">
<head>
<meta charset="utf-8">
<title>Meridian Commercial Realty — Home</title>
<link rel="stylesheet" href="https://fonts.googleapis.com/css2?family=Open+Sans:ital,wght@0,400;0,600;0,700;1,400;1,600&display=swap">
<style>
:root{
  --green:#138a56;
  --green-dark:#0f6f45;
  --ink:#222;
  --body:#444;
  --muted:#777;
  --page:#efefef;
  --rule:#d6d6d6;
  --footer:#3b3b3b;
  --footer-deep:#2a2a2a;
  --footer-text:#aaa;
  --field:#2a2a2a;
}
*{box-sizing:border-box;margin:0;padding:0}
html,body{width:767px;height:1200px;overflow:hidden}
body{position:relative;background:var(--page);font-family:"Open Sans",Arial,sans-serif;color:var(--body);font-size:8px;line-height:1.6}
.abs{position:absolute}
a{color:inherit;text-decoration:none}

/* header */
.site-header{left:0;top:0;width:767px;height:75px;background:linear-gradient(#fbfbfb,#e9e9e9);border-bottom:1px solid #d8d8d8}
.brand{left:78px;top:22px;display:flex;align-items:center;gap:6px}
.brand-mark{width:12px;height:12px;background:var(--green)}
.brand-name{font-size:26px;font-weight:700;color:var(--green);letter-spacing:-.5px;line-height:1}
.brand-sub{left:78px;top:52px;font-size:5.5px;font-weight:700;color:var(--green);letter-spacing:.1px}
.main-nav{left:286px;top:0;display:flex;height:75px}
.main-nav a{display:flex;align-items:center;padding:0 14px;font-size:10px;color:#444;height:75px;padding-top:4px}
.main-nav a.active{background:#fff;color:var(--green);width:58px;justify-content:center;padding:4px 0 0;margin-right:3px;box-shadow:0 0 4px rgba(0,0,0,.08)}

/* hero */
.hero{left:0;top:75px;width:767px;height:234px;background:linear-gradient(180deg,#b9cfe0 0%,#d3dde5 35%,#8b939a 70%,#5f6568 100%)}
.hero-card{left:78px;top:134px;width:267px;height:124px;background:rgba(19,138,86,.9);color:#fff;text-align:center;padding-top:12px}
.hero-card h1{font-weight:400;font-size:16.5px;line-height:1.2}
.hero-card .tag{font-size:7.8px;font-weight:600;margin-top:2px}
.hero-card .call{font-size:15.5px;margin-top:8px;line-height:1.2}
.hero-card .phone{font-size:23px;line-height:1.2}
.slider-band{left:0;top:309px;width:767px;height:21px;background:linear-gradient(#e2e2e2,#ececec)}
.dots{left:359px;top:315px;display:flex;gap:6px}
.dots span{width:11px;height:11px;border-radius:50%;background:#cfcfcf;box-shadow:inset 0 1px 2px rgba(0,0,0,.25)}
.dots span.on{background:var(--green)}

/* features */
.feature{top:370px;width:190px}
.feature-head{display:flex;gap:6px;align-items:flex-start;height:45px}
.feature-head h3{font-size:11.5px;font-weight:400;line-height:1.35;color:var(--ink);padding-top:1px}
.feature-head h3.green{color:var(--green)}
.feature p{font-size:7.6px;color:#555;margin-top:-1px}
.more{font-size:7.6px;color:#333;margin-top:4px;display:block}
.more.green{color:var(--green)}
.vrule{top:364px;width:1px;height:118px;background:var(--rule)}

/* section headings */
.sec-title{font-size:13px;color:var(--ink);display:flex;align-items:center;gap:8px;font-weight:400}
.sec-title::after{content:"";flex:1;height:6px;background:repeating-linear-gradient(135deg,#d9d9d9 0 1px,transparent 1px 3px)}
.side-title{font-size:11px}

/* about */
.about{left:78px;top:520px;width:388px}
.about .lead{font-style:italic;font-weight:600;font-size:7.5px;color:#444;margin-top:9px;line-height:1.75}
.about-body{display:flex;gap:8px;margin-top:9px}
.about-photo{width:95px;height:75px;flex:none;background:linear-gradient(135deg,#c7ccd0,#8f9aa3 60%,#6e6a66)}
.about-body p{font-size:7.5px;line-height:1.75;color:#444}

/* tabs */
.tabs{left:78px;top:719px;display:flex;gap:3px}
.tab{height:34px;padding:0 14px;display:flex;align-items:center;font-size:11px}
.tab.on{background:var(--green);color:#fff}
.tab.off{background:#fff;color:var(--ink);border:1px solid #ddd;border-bottom:none;height:33px;margin-top:1px;padding:0 14px}
.tab-panel{left:77px;top:752px;width:388px;height:152px;background:#fff;border:1px solid #e0e0e0;padding:9px 12px}
.tab-panel .lead{font-style:italic;font-weight:600;font-size:7.5px;line-height:1.75;color:#444}
.tab-panel ul{list-style:none;margin-top:6px}
.tab-panel li{font-size:7.5px;line-height:2.2;color:#444;display:flex;gap:6px;white-space:nowrap;overflow:hidden}
.tab-panel li::before{content:"\2192";color:#222}
.tab-panel .more{text-align:right;margin-top:1px}

/* sidebar */
.sidebar{left:500px;top:520px;width:190px}
.deal{display:flex;gap:9px;margin-top:14px}
.deal + .deal{margin-top:16px}
.deal-photo{width:53px;height:48px;flex:none;border:2px solid #ccc;background:linear-gradient(160deg,#c9c6c1,#8b8680)}
.deal h4{font-size:8px;font-weight:600;color:var(--green);line-height:1.4}
.deal p{font-size:7.5px;line-height:1.5;color:#444}
.deal b{font-weight:600;color:#222}
.more-deals{display:block;text-align:right;font-size:7.5px;color:var(--green);text-decoration:underline;margin-top:6px}
.hr{height:1px;background:var(--rule);margin-top:10px}
.follow{display:flex;align-items:center;gap:6px;margin-top:14px}
.follow span.label{font-size:11.5px;color:var(--green);margin-right:2px}
.follow i{width:20px;height:20px;background:#9a9a9a;border-radius:2px;display:block}
.follow i.on{background:#3b67c2}
.contact-info{margin-top:18px}
.contact-info h3{font-size:11px;font-weight:400;color:var(--ink)}
.contact-info p{font-size:8px;color:#333;line-height:1.6;margin-top:3px}
.ci-row{display:flex;align-items:center;gap:8px;font-size:8.5px;color:#333;margin-top:7px}

.landmark{opacity:.35}

/* footer */
.site-footer{left:0;top:959px;width:767px;height:201px;background:var(--footer)}
.fcol{top:983px}
.fcol h5{font-size:11.5px;font-weight:600;color:#222;padding-bottom:6px;border-bottom:1px solid #4d4d4d}
.fcol ul{list-style:none;margin-top:6px}
.fcol li{font-size:7.5px;line-height:2.2;color:var(--footer-text)}
.fcol li.cur{color:#fff}
.fcol li.u{color:#eee;text-decoration:underline}
.quote{width:140px;height:70px;background:var(--footer-deep);color:#ccc;font-size:7.5px;line-height:1.55;padding:10px 9px;margin-top:14px;position:relative}
.quote::after{content:"";position:absolute;left:28px;bottom:-12px;border-left:12px solid var(--footer-deep);border-bottom:12px solid transparent}
.person{display:flex;gap:8px;margin-top:16px;align-items:center}
.avatar{width:22px;height:30px;background:#222}
.person b{display:block;color:#eee;font-size:8.5px;font-weight:600}
.person span{color:var(--footer-text);font-size:7.5px}
.form-row{display:flex;justify-content:space-between;margin-top:9px;font-size:7.5px;color:var(--footer-text)}
.field{width:102px;height:19px;background:var(--field);border:1px solid #222;border-radius:2px}
.field.tall{height:43px}
.btn{margin-top:9px;margin-left:90px;width:50px;height:20px;background:#777;border:1px solid #999;color:#222;font-size:7.5px;font-weight:700;display:flex;align-items:center;justify-content:center}
.legal{left:0;top:1160px;width:767px;height:40px;background:#2b2b2b;color:#888;font-size:7.5px;text-align:center;line-height:40px}
</style>
</head>
<body>

<header class="site-header abs">
</header>
<div class="brand abs"><span class="brand-mark"></span><span class="brand-name">MCR</span></div>
<div class="brand-sub abs">MERIDIAN COMMERCIAL REALTY</div>
<nav class="main-nav abs">
  <a class="active" href="#">HOME</a>
  <a href="#">ABOUT US</a>
  <a href="#">SERVICES</a>
  <a href="#">RESEARCH</a>
  <a href="#">FAQ</a>
  <a href="#">CONTACT US</a>
</nav>

<section class="hero abs" role="img" aria-label="Photo of a city skyline with office towers under a pale sky"></section>
<div class="hero-card abs">
  <h1>Meridian Commercial Realty</h1>
  <div class="tag">is a small commercial real estate firm in the Washington DC</div>
  <div class="call">Call Us for quick Information</div>
  <div class="phone">0000 000 000</div>
</div>
<div class="slider-band abs"></div>
<div class="dots abs"><span class="on"></span><span></span><span></span></div>

<div class="feature abs" style="left:78px">
  <div class="feature-head">
    <svg width="34" height="34" viewBox="0 0 34 34"><rect x="1" y="1" width="32" height="32" rx="2" fill="none" stroke="#138a56" stroke-width="2"/><rect x="5" y="5" width="24" height="24" fill="#138a56"/><g fill="#fff"><rect x="8" y="8" width="4" height="4"/><rect x="14" y="8" width="12" height="4"/><rect x="8" y="15" width="4" height="4"/><rect x="14" y="15" width="12" height="4"/><rect x="8" y="22" width="4" height="4"/><rect x="14" y="22" width="12" height="4"/></g></svg>
    <h3 class="green">List and reach for<br>monthly visitors</h3>
  </div>
  <p>Lorem ipsum dolor sit amet, consectetur<br>adipiscing elit.</p>
  <a class="more green" href="#">&rarr; Read More</a>
</div>
<div class="vrule abs" style="left:277px"></div>
<div class="feature abs" style="left:318px">
  <div class="feature-head">
    <svg width="36" height="38" viewBox="0 0 36 38"><circle cx="14" cy="14" r="10" fill="none" stroke="#8a8a8a" stroke-width="4"/><line x1="21" y1="22" x2="32" y2="34" stroke="#8a8a8a" stroke-width="6" stroke-linecap="round"/></svg>
    <h3>Search of property<br>for lease</h3>
  </div>
  <p>Lorem ipsum dolor sit amet, consectetur<br>adipiscing elit.</p>
  <a class="more" href="#">&rarr; Read More</a>
</div>
<div class="vrule abs" style="left:500px"></div>
<div class="feature abs" style="left:542px">
  <div class="feature-head">
    <svg width="34" height="34" viewBox="0 0 34 34"><path d="M14 3H2v29h29V20" fill="none" stroke="#8a8a8a" stroke-width="3"/><path d="M10 22c2-8 8-11 15-11V6l8 8-8 8v-5c-6 0-11 1-15 5z" fill="#8a8a8a"/></svg>
    <h3>Learn more about<br>our services</h3>
  </div>
  <p>Lorem ipsum dolor sit amet, consectetur<br>adipiscing elit.</p>
  <a class="more" href="#">&rarr; Read More</a>
</div>

<section class="about abs">
  <h2 class="sec-title">About Us</h2>
  <p class="lead">Lorem ipsum dolor sit amet, consectetur adipiscing elit. Nulla lobortis consequat mauris, eget eleifend nunc viverra viverra. Ut ac risus odio. Aliquam pretium purus sed nulla feugiat blandit.</p>
  <div class="about-body">
    <div class="about-photo" role="img" aria-label="Photo of a small team reviewing work at an office desk"></div>
    <div>
      <p>Lorem ipsum dolor sit amet, consectetur adipiscing elit. Nulla lobortis consequat mauris, eget eleifend nunc viverra viverra. Ut ac risus odio. Aliquam pretium purus sed nulla feugiat blandit. Cras vel libero ut lacus eleifend tempor. Phasellus eleifend.</p>
      <a class="more green" href="#">&rarr; Read More</a>
    </div>
  </div>
</section>

<div class="tabs abs"><span class="tab on">How we can help you</span><span class="tab off">MCR News</span></div>
<div class="tab-panel abs">
  <p class="lead">Lorem ipsum dolor sit amet, consectetur adipiscing elit. Nulla lobortis consequat mauris, eget eleifend nunc viverra viverra. Ut ac risus odio. Aliquam pretium purus sed nulla feugiat blandit.</p>
  <ul>
    <li>Lorem ipsum dolor sit amet, consectetur adipiscing elit. Nulla lobortis consequat mauris, eget</li>
    <li>Eleifend nunc viverra viverra. Ut ac risus odio. Aliquam pretium purus sed nulla feugiat blandit. Cras</li>
    <li>Vel libero ut lacus eleifend tempor. Phasellus eleifend, magna non tincidunt accumsan, justo arcu</li>
    <li>Cursus ipsum, non porttitor sapien quam vel magna. Maecenas elit nisl, molestie nec dapibus nec</li>
  </ul>
  <a class="more green" href="#">&rarr; Read More</a>
</div>

<aside class="sidebar abs">
  <h2 class="sec-title side-title">Recent Transactions</h2>
  <div class="deal">
    <div class="deal-photo" role="img" aria-label="Photo of an open-plan office interior"></div>
    <div><h4>Office</h4><p><b>Client:</b> Brook &amp; Co<br>Lorem ipsum dolor sit amet,</p><a class="more green" href="#">&rarr; Read More</a></div>
  </div>
  <div class="deal">
    <div class="deal-photo" role="img" aria-label="Photo of a retail store interior"></div>
    <div><h4>Retail</h4><p><b>Client:</b> Brook &amp; Co<br>Lorem ipsum dolor sit amet,</p><a class="more green" href="#">&rarr; Read More</a></div>
  </div>
  <a class="more-deals" href="#">&rarr; More Recent Transaction</a>
  <div class="hr"></div>
  <div class="follow"><span class="label">Follow Us On:</span><i class="on" aria-label="Social link"></i><i aria-label="Social link"></i><i aria-label="Social link"></i><i aria-label="Social link"></i></div>
  <div class="hr" style="margin-top:12px"></div>
  <div class="contact-info">
    <h3>Contact Information</h3>
    <p>Meridian Commercial Realty<br>&nbsp;Washington DC</p>
    <div class="ci-row"><svg width="13" height="10" viewBox="0 0 13 10"><path d="M1 3c3-3 8-3 11 0l-2 2-2-1V3H5v1L3 5z" fill="#555"/><rect x="3" y="5" width="7" height="5" rx="1" fill="#555"/></svg>0000 000 000</div>
    <div class="ci-row"><svg width="13" height="9" viewBox="0 0 13 9"><rect x="0" y="0" width="13" height="9" fill="#666"/><path d="M0 0l6.5 5L13 0" fill="none" stroke="#eee" stroke-width="1"/></svg>hello@meridiancr.example</div>
  </div>
  <div class="hr" style="margin-top:10px"></div>
</aside>

<div class="landmark abs" style="left:18px;top:845px;width:145px;height:114px;background:linear-gradient(180deg,transparent,#d4d4d4)" role="img" aria-label="Faint drawing of a domed capitol building"></div>
<div class="landmark abs" style="left:700px;top:855px;width:50px;height:104px;background:linear-gradient(180deg,transparent,#d4d4d4)" role="img" aria-label="Faint drawing of an obelisk monument"></div>

<footer class="site-footer abs"></footer>
<div class="fcol abs" style="left:78px;width:80px">
  <h5>Quick Link</h5>
  <ul><li class="cur">HOME</li><li>ABOUT US</li><li>SERVICES</li><li>RESEARCH</li><li>&nbsp;FAQ</li><li>CONTACT US</li></ul>
</div>
<div class="fcol abs" style="left:200px;width:125px">
  <h5>Quick Search</h5>
  <ul><li>Business Management &amp; Productivity</li><li class="u">Real Estate Deal Analysis &amp; Advice</li><li>Real Estate</li><li>Opinion</li><li>Mortgages &amp; Lending</li><li>Real Estate Law</li></ul>
</div>
<div class="fcol abs" style="left:369px;width:140px">
  <h5>What Other Say</h5>
  <div class="quote">&#10077; Lorem ipsum dolor sit amet, consectetur adipiscing elit. Nulla lobortis consequat mauris, eget eleifend nunc viverra viverra. &#10078;</div>
  <div class="person"><div class="avatar" role="img" aria-label="Placeholder silhouette of the reviewer"></div><div><b>Alan Marsh</b><span>CEO Information Technology</span></div></div>
</div>
<div class="fcol abs" style="left:551px;width:140px">
  <h5>Contact with us</h5>
  <div class="form-row"><span>Name*</span><div class="field"></div></div>
  <div class="form-row" style="margin-top:4px"><span>Email*</span><div class="field"></div></div>
  <div class="form-row" style="margin-top:4px"><span>Message</span><div class="field tall"></div></div>
  <div class="btn">SEARCH</div>
</div>
<div class="legal abs">&copy;2013 meridiancr.example. All right reserved.</div>

</body>
</html>
```